Unique business card design

We are looking for a design that reflects our unique social media and online marketing agency "Kestrel Media". We are a young agency with a focus on speakers, coaches and trainers. In other words, we support people who want to do good with their work and help other people live a happier, more successful and fulfilling life, reach as many people as possible with their work and thus have an influence. Our values are: sustainability, creating added value, individuality, proactivity. We want our clients to feel comfortable with us and that's why the relationship with them is very important to us. We want every customer to become a lifelong friend of the company. Most of our clients are premium coaches, meaning they are in the higher priced segment and expect seriousness, professionalism and quality. All of these things should reflect our business card as well. I look forward to feedback. Best regards, Tomas Wylander

```html
<!DOCTYPE html>
<html lang="en">
<head>
<meta charset="utf-8">
<title>Kestrel Media — Business Card</title>
<link href="https://fonts.googleapis.com/css2?family=Questrial&display=swap" rel="stylesheet">
<style>
  :root {
    --backdrop: #3a3431;
    --card: #161616;
    --card-edge: #242424;
    --ink: #f2f2f2;
    --ink-soft: #d8d8d8;
    --accent: #1e6fd9;
    --accent-deep: #1a3fa8;
  }
  * { margin: 0; padding: 0; box-sizing: border-box; }
  html, body {
    width: 1200px;
    height: 780px;
    overflow: hidden;
    background: var(--backdrop);
    font-family: "Questrial", "Century Gothic", sans-serif;
  }
  .canvas {
    position: relative;
    width: 1200px;
    height: 780px;
    display: flex;
    align-items: center;
    justify-content: center;
    gap: 60px;
  }
  .card {
    position: relative;
    width: 525px;
    height: 300px;
    background: var(--card);
    border: 1px solid var(--card-edge);
    border-radius: 4px;
    box-shadow: 0 14px 30px rgba(0,0,0,0.45);
    color: var(--ink);
  }

  /* Front */
  .card--front .brand {
    position: absolute;
    left: 150px;
    top: 108px;
  }
  .brand__row {
    display: flex;
    align-items: center;
    gap: 12px;
  }
  .brand__square {
    width: 34px;
    height: 34px;
    background: var(--accent-deep);
  }
  .brand__name {
    font-size: 34px;
    color: var(--ink);
    letter-spacing: 0.2px;
    line-height: 1;
  }
  .brand__tagline {
    margin-top: 8px;
    font-size: 13px;
    color: var(--ink-soft);
    letter-spacing: 0.4px;
  }

  /* Back */
  .card--back .company {
    position: absolute;
    right: 36px;
    top: 58px;
    font-size: 40px;
    color: var(--ink);
    letter-spacing: 0.3px;
  }
  .person {
    position: absolute;
    left: 0;
    right: 0;
    top: 124px;
    text-align: center;
    padding-left: 90px;
  }
  .person__name {
    font-size: 17px;
    color: var(--ink);
    line-height: 1.1;
  }
  .person__role {
    font-size: 14px;
    color: var(--accent);
    line-height: 1.1;
  }
  .contacts {
    position: absolute;
    left: 0;
    right: 0;
    top: 178px;
    text-align: center;
    font-size: 14px;
    color: var(--ink-soft);
    line-height: 1.55;
  }
  .contacts__line {
    display: flex;
    justify-content: center;
    align-items: center;
    gap: 7px;
  }
  .contacts__divider {
    width: 1px;
    height: 13px;
    background: var(--accent);
    margin: 0 4px;
  }
  .icon { width: 12px; height: 12px; flex: none; }
  .icon path, .icon rect, .icon circle { stroke: var(--accent); fill: none; stroke-width: 1.4; }
  .icon .solid { fill: var(--accent); stroke: none; }
</style>
</head>
<body>
<main class="canvas">

  <section class="card card--front" aria-label="Card front">
    <div class="brand">
      <div class="brand__row">
        <span class="brand__square"></span>
        <span class="brand__name">Kestrel Media</span>
      </div>
      <p class="brand__tagline">Online Marketing Services</p>
    </div>
  </section>

  <section class="card card--back" aria-label="Card back">
    <h1 class="company">Kestrel Media</h1>

    <div class="person">
      <p class="person__name">Tomas Wylander</p>
      <p class="person__role">Founder</p>
    </div>

    <div class="contacts">
      <p class="contacts__line">
        <svg class="icon" viewBox="0 0 12 12" aria-hidden="true"><rect x="3" y="0.8" width="6" height="10.4" rx="1"/></svg>
        <span>(555) 214-8830</span>
        <span class="contacts__divider"></span>
        <svg class="icon" viewBox="0 0 12 12" aria-hidden="true"><rect class="solid" x="0.5" y="2" width="11" height="8"/><path d="M0.8 2.4 L6 6.6 L11.2 2.4" style="stroke:#161616"/></svg>
        <span>hello@kestrelmedia.com</span>
      </p>
      <p class="contacts__line">
        <svg class="icon" viewBox="0 0 12 12" aria-hidden="true"><circle class="solid" cx="6" cy="6" r="5.5"/><path d="M0.8 6 H11.2 M6 0.8 C3.5 3.5 3.5 8.5 6 11.2 M6 0.8 C8.5 3.5 8.5 8.5 6 11.2" style="stroke:#161616;stroke-width:0.9"/></svg>
        <span>www.kestrelmedia.com</span>
      </p>
      <p class="contacts__line">
        <span>PO Box 418, 27 Harbour Lane, Geelong</span>
      </p>
    </div>
  </section>

</main>
</body>
</html>
```